IT Company requires new Business Card design.

Over the years we have had a few different business card designs. We are now due for new cards across the board for all staff. We felt this would be a good time to start fresh with a new design. Our traditional card simply had our details on the front, and a list of services on the back. We don't particularly need the list of services, we have had cards where the only thing on the rear of the card was our logo.
Feel free to be creative, we would like our tag line "Complete IT Management" to appear at some point, doesn't necessarily have to be with the logo.
I have attached samples and drafts of various previous cards we have used over the years.

```html
<!DOCTYPE html>
<html lang="en">
<head>
<meta charset="utf-8">
<title>Complete IT Management – Services Card</title>
<link rel="stylesheet" href="https://fonts.googleapis.com/css2?family=Open+Sans:ital,wght@0,300;0,600;1,400&display=swap">
<style>
  :root {
    --card-blue: #0c67a8;
    --text-white: #ffffff;
  }
  html, body {
    margin: 0;
    padding: 0;
    width: 667px;
    height: 1200px;
    overflow: hidden;
    background: var(--card-blue);
  }
  .card {
    position: relative;
    width: 667px;
    height: 1200px;
    background: var(--card-blue);
    color: var(--text-white);
    font-family: "Open Sans", sans-serif;
  }
  .tagline {
    position: absolute;
    top: 80px;
    left: 0;
    width: 100%;
    margin: 0;
    text-align: center;
    font-weight: 600;
    font-size: 31px;
    line-height: 38px;
    letter-spacing: 0.2px;
  }
  .service-list {
    position: absolute;
    left: 118px;
    margin: 0;
    padding: 0;
    list-style: none;
    font-weight: 300;
    font-size: 25px;
    line-height: 37.8px;
  }
  .service-list--it { top: 248px; }
  .service-list--infrastructure { top: 504px; }
  .service-list--web { top: 763px; left: 120px; }
  .website {
    position: absolute;
    top: 1109px;
    left: 118px;
    margin: 0;
    font-style: italic;
    font-weight: 400;
    font-size: 25px;
    line-height: 38px;
    letter-spacing: 1.3px;
  }
</style>
</head>
<body>
  <main class="card">
    <h1 class="tagline">COMPLETE IT MANAGEMENT</h1>

    <ul class="service-list service-list--it">
      <li>Networking</li>
      <li>Servers</li>
      <li>Workstations</li>
      <li>Laptops</li>
      <li>Firewalls</li>
    </ul>

    <ul class="service-list service-list--infrastructure">
      <li>Data Cabling</li>
      <li>All electrical Work</li>
      <li>Server Racks</li>
      <li>Network Infrastructure</li>
      <li>Off site back up</li>
    </ul>

    <ul class="service-list service-list--web">
      <li>ADSL Connections</li>
      <li>Web Hosting</li>
      <li>Web Design</li>
      <li>Website Maintenance</li>
      <li>Domain Names PABX systems</li>
    </ul>

    <p class="website">www.harbourlinknetworks.com.au</p>
  </main>
</body>
</html>
```